Graphic or Colorful Core Values Wall

I need artwork for an executive conference room wall. It is the blank space between the window and bookshelf (some photos have a blue 24x48 paper taped to the wall). I'm open to material options. The room has metal, wood, acrylic, black, silver, navy blue, saddle leather chairs, and a white conference table. There will be a sideboard/table below the artwork for balance. Not sure what that'll look like yet. You can see the mockups in the pdfs. You can read more about our heritage at dervy.com. <-- Feel free to use imagery from here if need be.

We have been around since 1929 so anything historical is fair game. We built the shell-shaped marlin station in Winston-Salem, NC (only 1 remains today) However we have diversified greatly since then.

Target Market(s)

Executives

Font styles to use
Sans Serif
Other font styles liked:
• Century Gothic for the main font, "Since 1929" is in Jelytta

Requirements
Must have
• The artwork or graphic must include the following Core Values: do it because it is right treat customers, vendors, and fellow employees as we would like to be treated be financially responsible be better today than yesterday Vision: To be the best at what we choose to do as recognized by our co-workers, customers, and competitors. Mission: To expand and develop our company through strict adherence to our "Core Ideology." We will empower, train, and motivate "Quality People" to strive for operational excellence.
Nice to have
• Owner likes color but the room doesn't have much color. Our logo has Red: #E10920 and Yellow: #FCBF15 in it
Should not have
• Look through our website and see how we use primary colors. We need to stay on brand as well as fit the room.

```html
<!DOCTYPE html>
<html lang="en">
<head>
<meta charset="utf-8">
<title>Core Values Wall Panel</title>
<link href="https://fonts.googleapis.com/css2?family=Didact+Gothic&family=Poppins:wght@400;500;600;700;800&family=Allura&display=swap" rel="stylesheet">
<style>
  :root {
    --canvas-bg: #c6c6c6;
    --panel-bg: #2f3139;
    --map-tone: #3a3c44;
    --brand-red: #E10920;
    --brand-yellow: #FCBF15;
    --white: #ffffff;
  }
  * { margin: 0; padding: 0; box-sizing: border-box; }
  html, body {
    width: 750px; height: 1200px; overflow: hidden;
    background: var(--canvas-bg);
  }
  .panel {
    position: absolute; left: 20px; top: 422px;
    width: 710px; height: 355px;
    background: var(--panel-bg);
    box-shadow: 6px 8px 10px rgba(0,0,0,0.35);
    overflow: hidden;
    font-family: "Poppins", sans-serif;
    color: var(--white);
  }
  .world-map {
    position: absolute; left: 20px; top: 20px; width: 660px; height: 320px;
    background: radial-gradient(ellipse at 50% 55%, var(--map-tone) 0%, rgba(58,60,68,0.5) 45%, rgba(47,49,57,0) 75%);
  }
  .headings { position: absolute; inset: 0; }
  .block { position: absolute; line-height: 1; white-space: nowrap; }
  .thin { font-family: "Didact Gothic", sans-serif; font-weight: 400; }
  .bold { font-weight: 700; }
  .yellow { color: var(--brand-yellow); }
  .red { color: var(--brand-red); }

  /* Core values column */
  .value-do { left: 40px; top: 107px; font-size: 20px; }
  .value-because { left: 40px; top: 134px; font-size: 14px; }
  .value-right { left: 40px; top: 150px; font-size: 21px; }
  .value-treat { left: 40px; top: 178px; font-size: 13.5px; }
  .value-treat-detail { left: 41px; top: 196px; font-size: 11px; line-height: 13.3px; }
  .value-financially { left: 41px; top: 238px; font-size: 18px; }
  .value-responsible {
    left: 41px; top: 261px; width: 128px; height: 18px;
    background: var(--brand-red);
    font-family: "Didact Gothic", sans-serif;
    font-size: 13px; letter-spacing: 2.2px; line-height: 18px; text-align: center;
  }
  .value-better { left: 42px; top: 287px; font-size: 11px; line-height: 13.5px; }

  /* Vision column */
  .vision-to-be { left: 238px; top: 107px; font-size: 20px; }
  .vision-best { left: 238px; top: 134px; font-size: 26px; font-weight: 800; }
  .vision-what { left: 238px; top: 170px; font-size: 20px; }
  .vision-choose { left: 238px; top: 194px; font-size: 14px; line-height: 17.5px; }
  .vision-audience { left: 238px; top: 228px; font-size: 20px; font-weight: 700; line-height: 27px; }

  /* Mission column */
  .brand-name {
    left: 518px; top: 48px; width: 152px; text-align: right;
    font-size: 24px; font-weight: 800; color: var(--brand-red); letter-spacing: -0.5px;
  }
  .brand-since {
    left: 600px; top: 80px; width: 68px; text-align: right;
    font-family: "Allura", cursive; font-size: 11px; color: #8a8c93;
  }
  .mission-text {
    right: 38px; top: 215px; font-size: 10px; font-weight: 600; line-height: 12.5px; text-align: right;
  }
  .mission-ideology { right: 38px; top: 242px; font-size: 17px; font-weight: 700; }
  .mission-empower { right: 38px; top: 264px; font-size: 8.6px; font-weight: 600; }
  .mission-people { right: 38px; top: 275px; font-size: 20px; font-weight: 700; }
  .mission-excellence {
    right: 38px; top: 300px; font-family: "Didact Gothic", sans-serif;
    font-size: 8.6px; letter-spacing: 3.1px; margin-right: -3px;
  }
  .quote-mark { color: var(--brand-red); font-family: "Didact Gothic", sans-serif; font-weight: 400; margin-right: 2px; }
</style>
</head>
<body>
  <section class="panel">
    <div class="world-map" role="img" aria-label="Faint dotted world map in the background"></div>

    <svg class="headings" viewBox="0 0 710 355" width="710" height="355" aria-hidden="false">
      <defs>
        <clipPath id="mission-band-clip">
          <rect x="424" y="149" width="246" height="59"/>
        </clipPath>
      </defs>
      <text x="34" y="99.5" font-family="Didact Gothic, sans-serif" font-size="74" fill="#ffffff" textLength="186" lengthAdjust="spacingAndGlyphs">CORE</text>
      <text x="244" y="99.5" font-family="Poppins, sans-serif" font-weight="700" font-size="74" fill="#FCBF15" textLength="255" lengthAdjust="spacingAndGlyphs">VALUES</text>
      <text x="670" y="141" text-anchor="end" font-family="Poppins, sans-serif" font-weight="700" font-size="60" fill="#ffffff" textLength="130" lengthAdjust="spacingAndGlyphs">OUR</text>
      <rect class="mission-band" x="424" y="149" width="246" height="59" fill="#E10920"/>
      <g clip-path="url(#mission-band-clip)">
        <text x="426" y="206" font-family="Poppins, sans-serif" font-weight="800" font-size="78" fill="#2f3139" textLength="242" lengthAdjust="spacingAndGlyphs">MISSION</text>
      </g>
      <g transform="translate(228,311) rotate(-90)">
        <text x="0" y="0" font-size="34" textLength="200" lengthAdjust="spacingAndGlyphs"><tspan font-family="Didact Gothic, sans-serif" fill="#ffffff">OUR </tspan><tspan font-family="Poppins, sans-serif" font-weight="700" fill="#FCBF15">VISION</tspan></text>
      </g>
    </svg>

    <!-- Core values -->
    <p class="block value-do bold">DO IT</p>
    <p class="block value-because thin">BECAUSE IT IS</p>
    <p class="block value-right bold yellow">RIGHT</p>
    <p class="block value-treat thin">TREAT CUSTOMERS</p>
    <p class="block value-treat-detail">vendors, and fellow<br>employees as we would<br>like to be treated be</p>
    <p class="block value-financially bold yellow">FINANCIALLY</p>
    <p class="block value-responsible">RESPONSIBLE</p>
    <p class="block value-better">be better today<br>than <b>YESTERDAY</b></p>

    <!-- Vision -->
    <p class="block vision-to-be">To be</p>
    <p class="block vision-best">THE BEST</p>
    <p class="block vision-what">at what we</p>
    <p class="block vision-choose yellow">choose to do as<br>recognized by our</p>
    <p class="block vision-audience">co-workers,<br>customers, <span class="thin">&amp;</span><br>competitors</p>

    <!-- Brand and mission -->
    <p class="block brand-name">Dervy Fuel</p>
    <p class="block brand-since">Since 1929</p>
    <p class="block mission-text">To expand and develop our company through<br>strict adherence to our</p>
    <p class="block mission-ideology yellow"><span class="quote-mark">“</span>CORE IDEOLOGY</p>
    <p class="block mission-empower">We will empower, train, and motivate</p>
    <p class="block mission-people yellow"><span class="quote-mark">“</span>QUALITY PEOPLE</p>
    <p class="block mission-excellence">TO STRIVE FOR OPERATIONAL EXCELLENCE</p>
  </section>
</body>
</html>
```